Letterhead for New Orthopaedic Surgery Practice

My husband and I are starting our own practice named RB Spine & Vitality Center. We would like to create a nice simple but high class letterhead that doesn't use too much solid color ink when printing. I like the colors dark blue, gold, yellow. Open to other suggestions. We will need to list him and I both on the top of the letterhead. Here is the important information:
Lucinda Perrow, M.D. - Hand and Upper Extremity Surgery
Abena Quist, M.D. - Hip & Knee Replacement/General Orthopaedic Surgery
Location: 18735 North Harlow Pkwy
Larkfield, FL 33482
Phone: 954-218-4650
Fax: 954-582-1346
Email: info@myrbspine.com

The only thing is that the phone and fax numbers will change once we get into our space. I just want to get the design started. I am including several documents which are my previous practice letterhead, my current procedure room letterhead, and our new Logo. The other letterheads are just for examples but please think outside of the box! We would love to see some great designs.

Colors
0054AA
0677BA
7BADD7
CADEEF
E8F1F8
0094D4
00A9DD
6FCCEA
C7EBF8
E9F6FB

Requirements
Must have
• class, elegance, luxury

```html
<!DOCTYPE html>
<html lang="en">
<head>
<meta charset="utf-8">
<title>RB Spine &amp; Vitality Center — Letterhead</title>
<link rel="stylesheet" href="https://fonts.googleapis.com/css2?family=Lora:ital,wght@0,400;0,600;1,600&display=swap">
<style>
  :root {
    --backdrop: #ececec;
    --paper: #ffffff;
    --navy: #1b2a4e;
    --gold: #d4a24c;
    --gold-soft: rgba(212, 162, 76, 0.22);
    --mist: rgba(190, 190, 195, 0.28);
  }
  * { margin: 0; padding: 0; box-sizing: border-box; }
  html, body {
    width: 1200px; height: 1200px; overflow: hidden;
    background: var(--backdrop);
    font-family: "Lora", Georgia, serif;
    color: var(--navy);
  }
  .sheet {
    position: absolute; left: 226px; top: 72px;
    width: 746px; height: 1054px;
    background: var(--paper);
    overflow: hidden;
  }
  .contour-gold {
    position: absolute; right: 0; top: 0;
    width: 340px; height: 170px;
    background: radial-gradient(ellipse at 100% 30%, var(--gold-soft) 0%, rgba(212,162,76,0.08) 55%, rgba(212,162,76,0) 75%);
  }
  .contour-grey {
    position: absolute; left: 0; bottom: 0;
    width: 746px; height: 430px;
    background: radial-gradient(ellipse at 75% 100%, var(--mist) 0%, rgba(190,190,195,0.12) 50%, rgba(190,190,195,0) 78%);
  }
  .brand {
    position: absolute; left: 50%; top: 52px;
    width: 144px; height: 144px; margin-left: -72px;
    border: 1.5px solid var(--gold);
    border-radius: 50%;
    display: flex; align-items: center; justify-content: center;
  }
  .brand-name {
    font-weight: 600; font-size: 13px; line-height: 1.45;
    letter-spacing: 2px; text-transform: uppercase; text-align: center;
    color: var(--navy);
  }
  .physicians {
    position: absolute; left: 37px; top: 970px;
    font-size: 12.5px; line-height: 15px;
  }
  .physician-name { font-style: italic; font-weight: 600; }
  .contact {
    position: absolute; right: 38px; top: 948px;
    list-style: none; text-align: right;
    font-size: 12.5px; line-height: 15px;
  }
  .contact li { display: flex; justify-content: flex-end; align-items: center; gap: 9px; }
  .contact svg { width: 8px; height: 9px; fill: var(--navy); }
</style>
</head>
<body>
  <main class="sheet">
    <div class="contour-gold" role="img" aria-label="Gold flowing contour line pattern in the top corner"></div>
    <div class="contour-grey" role="img" aria-label="Soft grey flowing contour line pattern across the lower page"></div>

    <header class="brand">
      <p class="brand-name">RB Spine &amp;<br>Vitality<br>Center</p>
    </header>

    <section class="physicians">
      <p><span class="physician-name">Lucinda Perrow</span>, M.D. - Hand and Upper Extremity Surgery</p>
      <p><span class="physician-name">Abena Quist</span>, M.D. - Hip &amp; Knee Replacement/General Orthopaedic Surgery</p>
    </section>

    <ul class="contact">
      <li>18735 North Harlow Pkwy
        <svg viewBox="0 0 8 10"><path d="M4 0a3 3 0 0 1 3 3c0 2.2-3 7-3 7S1 5.2 1 3a3 3 0 0 1 3-3zm0 1.9a1.1 1.1 0 1 0 0 2.2 1.1 1.1 0 0 0 0-2.2z"/></svg></li>
      <li>Larkfield, FL 33482 <svg viewBox="0 0 8 10"></svg></li>
      <li>954-218-4650
        <svg viewBox="0 0 8 9"><path d="M1.6 0.5l1.2 1.6-0.7 1c0.5 1.1 1.3 1.9 2.4 2.5l1-0.7 1.6 1.3-0.9 1.4C3.4 7.3 0.6 4.5 0.4 1.3z"/></svg></li>
      <li>954-582-1346
        <svg viewBox="0 0 8 9"><path d="M2 0h4v2.5H2zM0.5 3h7v4h-1.3v2H1.8V7H0.5zm2.2 3v2h2.6V6z"/></svg></li>
      <li>info@myrbspine.com
        <svg viewBox="0 0 8 9"><path d="M0.3 2h7.4v5H0.3zm0.8 0.8L4 5l2.9-2.2z" fill-rule="evenodd"/></svg></li>
    </ul>
  </main>
</body>
</html>
```